Website for Excavator and Earthworks Company

We require a modern, sleek and practical website for our newly created earthworks/excavator business in Perth, Western Australia called Gullwind Stonecut Earthworks.

The website should have a modern, cutting edge feel but only needs to be relatively simplistic in it's layout and eventual functionality.

Some pages it should have would be Home, About, Projects and Contact Us.

Number of Pages Required

1 page

```html
<!DOCTYPE html>
<html lang="en">
<head>
<meta charset="utf-8">
<title>Gullwind Stonecut Earthworks</title>
<link href="https://fonts.googleapis.com/css2?family=Exo+2:wght@600;700&family=Roboto:wght@400;500;700&display=swap" rel="stylesheet">
<style>
:root{
  --green:#bcd40c;
  --green-dark:#a6bc06;
  --ink:#111111;
  --night:#0d0d0d;
  --text:#555555;
  --white:#ffffff;
  --line:#e2e2e2;
}
*{box-sizing:border-box;margin:0;padding:0}
html,body{width:1200px;height:5296px;overflow:hidden}
body{position:relative;font-family:"Roboto",sans-serif;color:var(--ink);background:var(--white)}
.abs{position:absolute}
.heading{font-family:"Exo 2",sans-serif;font-weight:700;text-transform:uppercase;letter-spacing:1px;line-height:1}
.accent{color:var(--green)}
.btn{position:absolute;display:flex;align-items:center;justify-content:center;font-family:"Roboto",sans-serif;font-weight:700;font-size:14px;text-transform:uppercase}
.circle-arrow{position:absolute;border-radius:50%;display:flex;align-items:center;justify-content:center}

/* header */
.site-header{position:absolute;left:0;top:0;width:1200px;height:88px;background:var(--white);overflow:hidden}
.brand{position:absolute;left:40px;top:20px;display:flex;align-items:center;gap:10px}
.brand-mark{width:40px;height:40px;background:var(--green)}
.brand-name{font-family:"Exo 2",sans-serif;font-weight:700;font-size:20px;color:var(--ink);text-transform:uppercase;line-height:1.05;letter-spacing:.5px}
.main-nav{position:absolute;left:447px;top:32px;display:flex;gap:0;font-size:16px}
.main-nav span{position:absolute;white-space:nowrap}
.call-box{position:absolute;left:952px;top:0;width:248px;height:88px;background:var(--night);clip-path:polygon(28px 0,100% 0,100% 100%,0 100%)}
.call-icon{position:absolute;left:955px;top:24px;width:42px;height:42px;border-radius:50%;background:var(--green);display:flex;align-items:center;justify-content:center}
.call-text{position:absolute;left:1020px;top:24px;color:var(--white)}
.call-text small{display:block;font-size:12px}
.call-text strong{display:block;font-size:19px;color:var(--green);font-weight:700;margin-top:3px}

/* hero */
.hero{position:absolute;left:0;top:88px;width:1200px;height:607px;background:linear-gradient(180deg,#3b2f2a 0%,#6a4a34 35%,#3a2a1f 70%,#1c1712 100%)}
.hero-title{position:absolute;left:0;top:190px;width:1200px;text-align:center;color:var(--white);font-size:46px}
.hero-sub{position:absolute;left:300px;top:290px;width:600px;text-align:center;color:var(--white);font-size:16px;line-height:27px}
/* about */
.about-frame{left:107px;top:780px;width:338px;height:470px;background:var(--green)}
.about-photo{left:131px;top:806px;width:436px;height:444px;background:linear-gradient(180deg,#3d5a80 0%,#d98a3a 45%,#7b4a25 75%,#2c221b 100%)}
.experience{left:395px;top:1045px;width:203px;height:205px}
.section-title{font-size:50px}
.body-copy{font-size:14px;line-height:26.5px;color:var(--text);text-align:justify}

/* services */
.services{position:absolute;left:0;top:1355px;width:1200px;height:473px;background:var(--green)}
.service-card{position:absolute;top:1638px;width:311px;height:250px;background:var(--white);box-shadow:0 4px 12px rgba(0,0,0,.12);border-bottom:4px solid #cfcfcf;text-align:center}
.service-card h3{margin-top:70px;font-size:18px;font-weight:700}
.service-card p{margin:14px 24px 0;font-size:13px;line-height:23px;color:var(--text);text-align:justify;text-align-last:center}
.service-card.active{height:294px;border-bottom-color:var(--green)}
.hex-icon{position:absolute;top:-52px;left:108px;width:95px;height:105px}
.learn{display:inline-flex;align-items:center;gap:6px;margin-top:16px;font-size:13px;font-weight:700;text-decoration:underline}

/* why */
.ticks{position:absolute;left:111px;top:2348px;list-style:none;font-size:15px}
.ticks li{display:flex;align-items:center;gap:18px;height:34.5px}
.tri{width:0;height:0;border-top:7px solid transparent;border-bottom:7px solid transparent;border-left:13px solid var(--green)}

/* testimonials */
.reviews{position:absolute;left:0;top:2617px;width:1200px;height:540px;background:linear-gradient(180deg,#1a1a1a,#0f0f0f)}
.review{position:absolute;top:2796px;width:456px;height:212px;background:var(--white)}
.stars{position:absolute;left:30px;top:26px;color:var(--green);font-size:14px;letter-spacing:2px}
.review p{position:absolute;left:30px;top:54px;width:400px;font-size:13.5px;line-height:24px;color:var(--text)}
.review strong{position:absolute;left:30px;top:146px;font-size:15px}
.avatar{position:absolute;left:22px;top:178px;width:74px;height:74px;border-radius:50%;background:linear-gradient(180deg,#9aa3ad,#5b6570);border:4px solid var(--white)}
.quote-mark{position:absolute;right:12px;bottom:0;font-family:"Exo 2",sans-serif;font-size:120px;line-height:.8;color:#e4e4e4;font-weight:700}

/* projects */
.tile{position:absolute}

/* contact */
.contact{position:absolute;left:0;top:4340px;width:1200px;height:545px;background:var(--green)}
.field{position:absolute;background:var(--white);font-size:12px;color:#888;padding:15px 12px;display:flex;align-items:flex-start;gap:6px}

/* footer */
.site-footer{position:absolute;left:0;top:4885px;width:1200px;height:411px;background:var(--night);color:var(--white)}
.foot-nav{position:absolute;left:0;top:160px;width:1200px;text-align:center;font-size:14px;font-weight:700}
.foot-nav span{margin:0 22px}
.info{position:absolute;top:230px;display:flex;align-items:center;gap:20px}
.info-icon{width:60px;height:60px;border-radius:50%;background:var(--green);display:flex;align-items:center;justify-content:center}
.info h4{font-size:14px;font-weight:700;margin-bottom:8px}
.info p{font-size:13px;line-height:18px}
.copyright{position:absolute;left:111px;top:330px;font-size:13px}
.social{position:absolute;top:322px;width:28px;height:28px;border-radius:50%}
</style>
</head>
<body>

<!-- header -->
<header class="site-header">
  <div class="brand">
    <div class="brand-mark"></div>
    <div class="brand-name">Gullwind Stonecut<br>Earthworks</div>
  </div>
  <nav class="main-nav">
    <span style="left:0;color:var(--green)">Home</span>
    <span style="left:81px">About Us</span>
    <span style="left:185px">Our Services</span>
    <span style="left:319px">Projects</span>
    <span style="left:416px">Contact</span>
  </nav>
  <div class="call-box"></div>
  <div class="call-icon">
    <svg width="20" height="20" viewBox="0 0 24 24"><path fill="#111" d="M6.6 10.8a15 15 0 0 0 6.6 6.6l2.2-2.2c.3-.3.7-.4 1-.2 1.1.4 2.3.6 3.6.6.6 0 1 .4 1 1V20c0 .6-.4 1-1 1A17 17 0 0 1 3 4c0-.6.4-1 1-1h3.5c.6 0 1 .4 1 1 0 1.3.2 2.5.6 3.6.1.3 0 .7-.2 1z"/></svg>
  </div>
  <div class="call-text"><small>Call Us Today</small><strong>+61 8 5550 1427</strong></div>
</header>

<!-- hero -->
<section class="hero" role="img" aria-label="Excavator working at sunset on an earthworks site">
  <h1 class="heading hero-title">Raising the ground.<br>Building the future.</h1>
  <p class="hero-sub">Professional excavation and earthworks services across Perth and Western Australia. Built on precision, reliability, and modern equipment.</p>
  <div class="btn" style="left:406px;top:366px;width:189px;height:46px;background:var(--green);color:var(--ink)">View our work</div>
  <div class="btn" style="left:604px;top:366px;width:188px;height:46px;background:var(--white);color:var(--ink)">Get a quote</div>
  <div class="circle-arrow" style="left:37px;top:286px;width:38px;height:38px;background:rgba(0,0,0,.55)"><svg width="12" height="12" viewBox="0 0 12 12"><path d="M8 1 3 6l5 5" stroke="#fff" stroke-width="2" fill="none"/></svg></div>
  <div class="circle-arrow" style="left:1125px;top:286px;width:38px;height:38px;background:rgba(0,0,0,.55)"><svg width="12" height="12" viewBox="0 0 12 12"><path d="M4 1l5 5-5 5" stroke="#fff" stroke-width="2" fill="none"/></svg></div>
</section>

<!-- about -->
<section>
  <div class="abs about-frame"></div>
  <div class="abs about-photo" role="img" aria-label="Yellow backhoe loader lifting a bucket of earth under an orange sky"></div>
  <svg class="abs experience" viewBox="0 0 203 205">
    <polygon points="101.5,0 203,70 203,205 0,205 0,70" fill="#ffffff"/>
    <polygon points="101.5,12 191,74 191,193 12,193 12,74" fill="var(--green)"/>
    <text x="101.5" y="140" text-anchor="middle" font-family="Exo 2,sans-serif" font-weight="700" font-size="84" fill="#111">10</text>
    <text x="101.5" y="172" text-anchor="middle" font-family="Roboto,sans-serif" font-size="13" fill="#111">Years Experience</text>
  </svg>
  <h2 class="abs heading section-title" style="left:652px;top:823px">About <span class="accent">Us</span></h2>
  <p class="abs body-copy" style="left:652px;top:888px;width:436px">Lorem ipsum dolor sit amet, consectetur adipiscing elit, sed do eiusmod tempor incididunt ut labore et dolore magna aliqua. Ut enim ad minim veniam, quis nostrud exercitation ullamco laboris nisi ut aliquip ex ea commodo consequat. Duis aute irure dolor in reprehenderit in voluptate velit esse cillum dolore eu fugiat nulla pariatur. Excepteur sint occaecat cupidatat non proident, sunt in culpa qui officia deserunt mollit anim id est laborum. Lorem ipsum dolor sit amet, consectetur adipiscing elit, sed do eiusmod tempor incididunt ut labore et dolore magna aliqua. Ut enim ad minim veniam, quis nostrud exercitation ullamco laboris nisi</p>
  <div class="btn" style="left:652px;top:1180px;width:140px;height:42px;background:var(--green);font-size:13px">Contact us</div>
</section>

<!-- services -->
<section class="services">
  <h2 class="heading section-title" style="position:absolute;left:0;top:78px;width:1200px;text-align:center">Our Services</h2>
  <p style="position:absolute;left:300px;top:140px;width:600px;text-align:center;font-size:16px;line-height:27px">Lorem ipsum dolor sit amet, consectetur adipiscing elit, sed do eiusmod et dolore magna aliqua. Ut enim ad minim veniam</p>
</section>
<div class="circle-arrow" style="left:33px;top:1730px;width:42px;height:42px;background:rgba(255,255,255,.25)"><svg width="12" height="12" viewBox="0 0 12 12"><path d="M8 1 3 6l5 5" stroke="#fff" stroke-width="2" fill="none"/></svg></div>
<div class="circle-arrow" style="left:1125px;top:1730px;width:42px;height:42px;background:rgba(255,255,255,.25)"><svg width="12" height="12" viewBox="0 0 12 12"><path d="M4 1l5 5-5 5" stroke="#fff" stroke-width="2" fill="none"/></svg></div>

<article class="service-card" style="left:111px">
  <svg class="hex-icon" viewBox="0 0 95 105"><polygon points="47.5,0 95,26 95,79 47.5,105 0,79 0,26" fill="#111"/><g stroke="#fff" stroke-width="2" fill="none"><rect x="28" y="58" width="30" height="10" rx="5"/><path d="M34 58v-10h14l4 10M52 50l10-14 8 8-4 10"/></g></svg>
  <h3>Excavation &amp; Site Prep</h3>
  <p>Lorem ipsum dolor sit amet, consectetur adipiscing elit, sed do eiusmod tempor inci didunt ut labore et dolore magna aliqua. Ut enim ad minim veniam, quis nostrud exer citation ullamco</p>
</article>
<article class="service-card active" style="left:445px">
  <svg class="hex-icon" viewBox="0 0 95 105"><polygon points="47.5,0 95,26 95,79 47.5,105 0,79 0,26" fill="#111"/><g stroke="#fff" stroke-width="2" fill="none"><path d="M24 70h48M30 70l10-20h16l8 20M44 50l6-16 14 6"/><circle cx="62" cy="46" r="4"/></g></svg>
  <h3>Earthmoving &amp; Bulk Works</h3>
  <p>Lorem ipsum dolor sit amet, consectetur adipiscing elit, sed do eiusmod tempor inci didunt ut labore et dolore magna aliqua. Ut enim ad minim veniam, quis nostrud exer citation ullamco</p>
  <div class="learn">LEARN MORE <svg width="14" height="14" viewBox="0 0 14 14"><circle cx="7" cy="7" r="7" fill="#111"/><path d="M6 4l3 3-3 3" stroke="#fff" stroke-width="1.6" fill="none"/></svg></div>
</article>
<article class="service-card" style="left:777px">
  <svg class="hex-icon" viewBox="0 0 95 105"><polygon points="47.5,0 95,26 95,79 47.5,105 0,79 0,26" fill="#111"/><g stroke="#fff" stroke-width="2" fill="none"><path d="M47 30v14M38 44h18l-4 10h-10zM30 68h34M36 68l6-8h10l6 8"/></g></svg>
  <h3>Trenching &amp; Footings</h3>
  <p>Lorem ipsum dolor sit amet, consectetur adipiscing elit, sed do eiusmod tempor inci didunt ut labore et dolore magna aliqua. Ut enim ad minim veniam, quis nostrud exer citation ullamco</p>
</article>

<!-- why -->
<section>
  <h2 class="abs heading section-title" style="left:111px;top:2075px;line-height:60px">Why <span class="accent">Gullwind<br>Stonecut</span></h2>
  <p class="abs body-copy" style="left:111px;top:2198px;width:437px;font-size:15px;color:#333">Lorem ipsum dolor sit amet, consectetur adipiscing elit, sed do eiusmod tempor incididunt ut labore et dolore magna aliqua. Ut enim ad minim veniam, quis nostrud exercitation ullamco laboris nisi ut aliquip ex ea commodo consequat.</p>
  <ul class="ticks">
    <li><span class="tri"></span>Locally owned Perth business</li>
    <li><span class="tri"></span>Modern machinery &amp; skilled operators</li>
    <li><span class="tri"></span>Safety-first, clean job sites</li>
    <li><span class="tri"></span>On-time, on-budget delivery</li>
  </ul>
  <div class="abs" style="left:600px;top:2072px;width:489px;height:425px;background:linear-gradient(180deg,#35588a 0%,#b06a38 45%,#8a4a28 70%,#5a3a22 100%)" role="img" aria-label="Yellow excavator on a rocky quarry site"></div>
</section>

<!-- testimonials -->
<section class="reviews">
  <h2 class="heading section-title" style="position:absolute;left:0;top:106px;width:1200px;text-align:center;color:var(--white)">What our <span class="accent">clients say</span></h2>
  <svg class="abs" style="left:52px;top:272px" width="24" height="36" viewBox="0 0 24 36"><path d="M18 4 6 18l12 14" stroke="#fff" stroke-width="3" fill="none"/></svg>
  <svg class="abs" style="left:1124px;top:272px" width="24" height="36" viewBox="0 0 24 36"><path d="M6 4l12 14-12 14" stroke="#fff" stroke-width="3" fill="none"/></svg>
</section>
<div class="review" style="left:124px">
  <div class="stars">★★★★★</div>
  <p>Lorem ipsum dolor sit amet, consectetur adipiscing elit, sed do eiusmod tempor incididunt ut labore et dolore magna minim veniam, quis nostrud aliqua.</p>
  <strong>Priya Hollis</strong>
  <div class="quote-mark">“</div>
  <div class="avatar" role="img" aria-label="Client portrait"></div>
</div>
<div class="review" style="left:620px">
  <div class="stars">★★★★★</div>
  <p>Lorem ipsum dolor sit amet, consectetur adipiscing elit, sed do eiusmod tempor incididunt ut labore et dolore magna minim veniam, quis nostrud aliqua.</p>
  <strong>Marcus Teel</strong>
  <div class="quote-mark">“</div>
  <div class="avatar" role="img" aria-label="Client portrait"></div>
</div>

<!-- projects -->
<section>
  <h2 class="abs heading section-title" style="left:0;top:3240px;width:1200px;text-align:center">Our <span class="accent">Projects</span></h2>
  <div class="tile" style="left:111px;top:3326px;width:610px;height:294px;background:linear-gradient(180deg,#c9d3dc 0%,#8e8a80 45%,#6b5a45 100%)" role="img" aria-label="Excavator digging beside new houses"></div>
  <div class="tile" style="left:737px;top:3326px;width:352px;height:606px;background:linear-gradient(180deg,#3e78c8 0%,#8fb4e2 35%,#c99a5e 60%,#b5824a 100%)" role="img" aria-label="Motor grader levelling a sandy site"></div>
  <div class="tile" style="left:111px;top:3637px;width:296px;height:295px;background:linear-gradient(180deg,#2f6dbf 0%,#7aa6d9 40%,#9b8468 70%,#6f5c44 100%)" role="img" aria-label="Dump truck and loader on a cleared site"></div>
  <div class="tile" style="left:425px;top:3637px;width:296px;height:295px;background:linear-gradient(180deg,#a9bf3a,#8ea42a)" role="img" aria-label="Earthworks site with project preview overlay">
    <div style="position:absolute;left:12px;top:12px;right:12px;bottom:12px;border:2px solid rgba(255,255,255,.85)"></div>
    <svg style="position:absolute;left:128px;top:128px" width="40" height="40" viewBox="0 0 40 40"><circle cx="17" cy="17" r="13" stroke="#fff" stroke-width="3" fill="none"/><path d="M26 26l11 11M17 11v12M11 17h12" stroke="#fff" stroke-width="3"/></svg>
  </div>
  <div class="tile" style="left:111px;top:3945px;width:610px;height:295px;background:linear-gradient(180deg,#7e96a8 0%,#5d6a55 30%,#9a7650 65%,#6d4e33 100%)" role="img" aria-label="Small excavator working on a trench site"></div>
  <div class="tile" style="left:737px;top:3945px;width:352px;height:295px;background:linear-gradient(180deg,#c9d1d6 0%,#5c7a48 40%,#8d6b4b 100%)" role="img" aria-label="Operator in a mini excavator in a garden"></div>
</section>

<!-- contact -->
<section class="contact">
  <h2 class="heading section-title" style="position:absolute;left:0;top:78px;width:1200px;text-align:center">Contact Us</h2>
  <div class="abs" style="left:0;top:390px;width:1200px;height:155px;background:linear-gradient(180deg,rgba(120,140,0,0),rgba(110,130,0,.45))" role="img" aria-label="City skyline silhouette with harbour bridge"></div>
</section>
<div class="field" style="left:215px;top:4495px;width:379px;height:44px">👤&nbsp;First Name</div>
<div class="field" style="left:605px;top:4495px;width:379px;height:44px">👤&nbsp;Last Name</div>
<div class="field" style="left:215px;top:4553px;width:379px;height:44px">✉&nbsp;Email Address</div>
<div class="field" style="left:605px;top:4553px;width:379px;height:44px">✆&nbsp;Phone Number</div>
<div class="field" style="left:215px;top:4612px;width:769px;height:98px">✎&nbsp;Message</div>
<div class="btn" style="left:522px;top:4760px;width:156px;height:45px;background:var(--ink);color:var(--white)">Submit now</div>

<!-- footer -->
<footer class="site-footer">
  <div class="abs" style="left:0;top:84px;width:1200px;display:flex;justify-content:center;align-items:center;gap:14px">
    <div style="width:46px;height:46px;background:var(--green)"></div>
    <div style="font-family:'Exo 2',sans-serif;font-weight:700;font-size:28px;text-transform:uppercase;line-height:1">Gullwind Stonecut<br><span style="font-size:16px;letter-spacing:5px">Earthworks</span></div>
  </div>
  <div class="foot-nav"><span>HOME</span>/<span>ABOUT US</span>/<span>OUR SERVICES</span>/<span>PROJECTS</span>/<span>CONTACT US</span></div>
  <div class="info" style="left:115px">
    <div class="info-icon"><svg width="24" height="24" viewBox="0 0 24 24"><path fill="#111" d="M6.6 10.8a15 15 0 0 0 6.6 6.6l2.2-2.2c.3-.3.7-.4 1-.2 1.1.4 2.3.6 3.6.6.6 0 1 .4 1 1V20c0 .6-.4 1-1 1A17 17 0 0 1 3 4c0-.6.4-1 1-1h3.5c.6 0 1 .4 1 1 0 1.3.2 2.5.6 3.6.1.3 0 .7-.2 1z"/></svg></div>
    <div><h4>PHONE</h4><p>+61 8 5550 1427</p></div>
  </div>
  <div class="info" style="left:448px">
    <div class="info-icon"><svg width="22" height="26" viewBox="0 0 22 26"><path fill="#111" d="M11 0a9 9 0 0 0-9 9c0 7 9 17 9 17s9-10 9-17a9 9 0 0 0-9-9zm0 12.5A3.5 3.5 0 1 1 11 5.5a3.5 3.5 0 0 1 0 7z"/></svg></div>
    <div><h4>ADDRESS</h4><p>123, Lorem ipsum dolor sit<br>Sydney</p></div>
  </div>
  <div class="info" style="left:812px">
    <div class="info-icon"><svg width="24" height="18" viewBox="0 0 24 18"><rect width="24" height="18" rx="2" fill="#111"/><path d="M2 2l10 8 10-8" stroke="#bcd40c" stroke-width="2" fill="none"/></svg></div>
    <div><h4>EMAIL</h4><p>hello@gullwindstonecut.com.au</p></div>
  </div>
  <div class="abs" style="left:111px;top:310px;width:978px;height:1px;background:#2a2a2a"></div>
  <p class="copyright">2026 Copyrights - <span class="accent" style="text-decoration:underline">Gullwind Stonecut</span> | All Rights Reserved</p>
  <div class="social" style="left:985px;background:#2b2b2b"></div>
  <div class="social" style="left:1020px;background:var(--green)"></div>
  <div class="social" style="left:1055px;background:#2b2b2b"></div>
</footer>

</body>
</html>
```